Uprising SaaS company needs an attractive business card design

We're an uprising SaaS company who's attempting to attack the rigid car (insurance) claims management market in Europe.
We want to our mighty base order management system, listen to our clients to connect the smart ideas to build something even mightier.
We primarily focus on helping our customers manage their customers' claims/orders and get them resolved as smoothly as possible.
We'd like the business card design to express technical innovation and the fact that we connect smart ideas, as our company slogan indicates.
Contact Information for Business Card
Name, position, website, email, mobile, business address
Colors
Designer to choose colors to be used in the design.
Look and feel
Each slider illustrates characteristics of the customer's brand and the style your logo design should communicate.

```html
<!DOCTYPE html>
<html lang="en">
<head>
<meta charset="utf-8">
<title>veltrano business card</title>
<link rel="stylesheet" href="https://fonts.googleapis.com/css2?family=Poppins:wght@300;400&display=swap">
<style>
  :root {
    --backdrop: #2b2b2b;
    --teal-light: #28879d;
    --teal-dark: #19739a;
    --paper-light: #f4f4f4;
    --paper-dark: #e2e2e2;
    --logo-white: #e9eaea;
    --accent: #6bbacd;
    --ink: #5f5f5f;
    --ink-strong: #6a6a6a;
  }
  * { margin: 0; padding: 0; box-sizing: border-box; }
  html, body {
    width: 1200px;
    height: 1138px;
    overflow: hidden;
    background: var(--backdrop);
    font-family: "Poppins", sans-serif;
  }
  .canvas { position: relative; width: 1200px; height: 1138px; }
  .card {
    position: absolute;
    left: 273px;
    width: 620px;
    height: 376px;
    border-radius: 16px;
    overflow: hidden;
  }
  .card-front {
    top: 184px;
    background: linear-gradient(135deg, var(--teal-light) 0%, var(--teal-dark) 100%);
  }
  .card-back {
    top: 606px;
    background: linear-gradient(180deg, var(--paper-light) 0%, var(--paper-dark) 100%);
  }
  .front-wordmark {
    position: absolute;
    left: 0;
    right: 0;
    top: 138px;
    text-align: center;
    font-weight: 300;
    font-size: 80px;
    line-height: 1;
    letter-spacing: 1px;
    color: var(--logo-white);
  }
  .front-website {
    position: absolute;
    left: 300px;
    top: 238px;
    font-weight: 400;
    font-size: 15px;
    letter-spacing: 2px;
    color: var(--logo-white);
  }
  .person-name {
    position: absolute;
    left: 42px;
    top: 58px;
    font-weight: 400;
    font-size: 30px;
    line-height: 1.1;
    color: var(--accent);
  }
  .person-role {
    position: absolute;
    left: 42px;
    top: 94px;
    font-weight: 400;
    font-size: 17px;
    color: var(--ink);
  }
  .address {
    position: absolute;
    left: 42px;
    top: 204px;
    font-size: 17px;
    line-height: 24px;
    color: var(--ink);
  }
  .contact-list {
    position: absolute;
    left: 42px;
    top: 260px;
    list-style: none;
    font-size: 17px;
    line-height: 24px;
    color: var(--ink);
  }
  .contact-list li { display: flex; align-items: center; }
  .contact-icon { width: 16px; height: 16px; margin-right: 11px; flex: none; }
  .side-wordmark {
    position: absolute;
    left: 546px;
    top: 197px;
    transform: translate(-50%, -50%) rotate(-90deg);
    font-weight: 300;
    font-size: 62px;
    line-height: 1;
    white-space: nowrap;
    color: var(--ink-strong);
  }
  .base-band {
    position: absolute;
    left: 0;
    right: 0;
    bottom: 0;
    height: 11px;
    display: flex;
  }
  .base-band-left { flex: 1; background: var(--ink-strong); }
  .base-band-right { flex: 1; background: var(--accent); }
</style>
</head>
<body>
<main class="canvas">
  <section class="card card-front" aria-label="Card front">
    <div class="front-wordmark">veltrano</div>
    <div class="front-website">www.veltrano.com</div>
  </section>

  <section class="card card-back" aria-label="Card back">
    <h1 class="person-name">Jonas Keller</h1>
    <p class="person-role">Managing Director</p>
    <p class="address">Lindenweg 14b<br>10115 Berlin, Germany</p>
    <ul class="contact-list">
      <li>
        <svg class="contact-icon" viewBox="0 0 16 16" aria-hidden="true">
          <path d="M1 6c0-2 3-3 7-3s7 1 7 3v1h-3V5.5C11 5 9.5 4.8 8 4.8S5 5 4 5.5V7H1z" fill="#6bbacd"/>
          <path d="M4 8l2-2h4l2 2 1 6H3z" fill="#6bbacd"/>
          <circle cx="8" cy="10" r="1.6" fill="#eeeeee"/>
        </svg>
        +49 170 5550142
      </li>
      <li>
        <svg class="contact-icon" viewBox="0 0 16 16" aria-hidden="true">
          <rect x="1" y="3.5" width="14" height="9" fill="#6bbacd"/>
          <path d="M1 3.5l7 5 7-5M1 12.5l5-4.5M15 12.5l-5-4.5" fill="none" stroke="#eeeeee" stroke-width="1"/>
        </svg>
        info@veltrano.com
      </li>
      <li>
        <svg class="contact-icon" viewBox="0 0 16 16" aria-hidden="true">
          <circle cx="8" cy="8" r="6.5" fill="#6bbacd"/>
          <g fill="none" stroke="#eeeeee" stroke-width="0.8">
            <ellipse cx="8" cy="8" rx="3" ry="6.5"/>
            <path d="M1.5 8h13M2.5 5h11M2.5 11h11M8 1.5v13"/>
          </g>
        </svg>
        https://veltrano.com
      </li>
    </ul>
    <div class="side-wordmark">veltrano</div>
    <div class="base-band">
      <span class="base-band-left"></span>
      <span class="base-band-right"></span>
    </div>
  </section>
</main>
</body>
</html>
```